Psychotherapy Website - Based in London

I am a newly trained psychotherapist and need a new website for www.rosalindfaber.co.uk.

I offer therapy for addiction, relationships, trauma and many other issues people face in their lives.

I want the website to be welcoming, gentle, feminine and for people to feel safe.

I do not like a page site that scrolls through sections, rather each page should be separate. Here some examples that i like. Sectional rather than scrolled.

https://www.hettiemarsh.com/
https://www.thequietwardrooms.com/

The imagery should be around pink using the flower in the logo / wording and around the site:

Here is a link to the flower for ideas:
https://www.pictofind.net/search?q=pink+gerbera&rlz=2D4KQTW_en-GBGB415GB415&source=lnms&tbm=isch&sa=X&ved=7cvQRtrk482h3PxZTuKLmeNBwXW_1AtXpVlKDbOQBmFLB&biw=1500&bih=889&dpr=2

RosalindFaber
Compassionate Psychotherapy

Is the logo and subheader for the website. Please use a typeface for the name that is appealing and professional.

Type face similar NOT EXLUSIVLY - JUST AN IDEA like this:
https://glowtonicstudio.com/

Basic business card i created as a rough idea below.

I have also added the website copy.

The headers are

Homepage
About Me
Therapy
Common Questions
Blog
Contact Me

Target Market(s)

Clients who are dealing with stress, trauma, pain, addiction

Industry/Entity Type

Therapy and Psychology

Coding

Coded - Design and coding required

Number of Pages Required

5+ page

Font styles to use
Serif
Sans Serif
Script

Colors
0054AA
0677BA
7BADD7
CADEEF
E8F1F8
0094D4
00A9DD
6FCCEA
C7EBF8
E9F6FB
E54698
E96AAD
F1A4CE
F9D9EA
FCEFF6

Requirements
Must have
• Pink Gerbera Flower integrated into design
Nice to have
• Images but not to stock imagery. Needs to look authentic and natural
Should not have
• Stock images of people. Images are important but needs to feel REAL

```html
<!DOCTYPE html>
<html lang="en">
<head>
<meta charset="utf-8">
<title>Rosalind Faber – Compassionate Psychotherapy</title>
<link href="https://fonts.googleapis.com/css2?family=Playfair+Display:wght@400;700&family=Mulish:wght@400;600;700;800&display=swap" rel="stylesheet">
<style>
:root{
  --blue:#0677BA;
  --blue-bright:#00A9DD;
  --blue-deep:#0054AA;
  --navy:#0b3556;
  --ink:#1c1c1c;
  --text:#2a2a2a;
  --rule:#d4d4d4;
  --pink:#E54698;
  --pink-soft:#F1A4CE;
  --pink-pale:#FCEFF6;
  --white:#ffffff;
}
*{margin:0;padding:0;box-sizing:border-box}
html,body{width:1151px;height:1200px;overflow:hidden;background:var(--white)}
body{position:relative;font-family:'Mulish',sans-serif;color:var(--text)}
.abs{position:absolute}

.gerbera-left{left:0;top:0;width:125px;height:660px;
  background:radial-gradient(ellipse 90px 120px at 30px 340px,#e64f98 0%,#ef7ab5 45%,rgba(241,164,206,.35) 75%,rgba(255,255,255,0) 100%),
             radial-gradient(ellipse 40px 120px at 80px 120px,rgba(241,164,206,.6),rgba(255,255,255,0));}
.petals-top{left:140px;top:0;width:140px;height:105px;
  background:radial-gradient(ellipse 60px 55px at 60px 50px,rgba(241,164,206,.55),rgba(255,255,255,0))}
.petals-low{left:140px;top:512px;width:170px;height:80px;
  background:radial-gradient(ellipse 80px 40px at 70px 25px,rgba(233,106,173,.45),rgba(255,255,255,0))}
.gerbera-right{left:965px;top:985px;width:186px;height:169px;
  background:radial-gradient(ellipse 150px 150px at 170px 160px,#c8103f 0%,#e42c5a 45%,rgba(229,70,152,.3) 80%,rgba(255,255,255,0) 100%)}

.contact{display:flex;align-items:center;gap:7px;top:20px}
.contact .icon{width:23px;height:23px;background:var(--blue);border-radius:3px;display:flex;align-items:center;justify-content:center}
.contact small{display:block;font-size:9.5px;color:var(--ink)}
.contact strong{display:block;font-size:12.5px;font-weight:600;color:var(--ink);letter-spacing:.2px}
.contact-phone{left:125px}
.contact-email{left:854px}

.brand{left:487px;top:5px;width:177px;height:48px;text-align:left;padding:6px 10px}
.brand-name{font-family:'Playfair Display',serif;font-weight:700;font-size:17px;color:var(--navy);line-height:1.1}
.brand-tag{font-size:9.5px;color:var(--navy);margin-top:2px}

.nav{left:125px;top:66px;width:901px;height:26px;border-top:1px solid var(--rule);border-bottom:1px solid var(--rule);
  display:flex;justify-content:center;align-items:center;gap:32px;padding-left:120px}
.nav a{font-size:10px;color:var(--ink);text-decoration:none;letter-spacing:.1px}
.nav a.current{color:var(--blue)}

.hero{left:125px;top:105px;width:901px;height:406px;
  background:linear-gradient(180deg,#c9dbe3 0%,#8fb0c0 30%,#3c90ad 46%,#2a6f8a 60%,#123e57 100%)}
.hero-art{left:0;top:0;width:560px;height:406px;
  background:radial-gradient(ellipse 260px 110px at 280px 230px,rgba(90,140,60,.55),rgba(0,0,0,0)),
             linear-gradient(165deg,rgba(255,255,255,0) 55%,rgba(20,35,45,.75) 80%)}
.hero-copy{left:567px;top:96px;width:310px;color:var(--white)}
.hero-kicker{font-family:'Playfair Display',serif;font-weight:700;font-size:17px}
.hero-title{font-family:'Playfair Display',serif;font-weight:700;font-size:38px;line-height:40px;margin-top:5px}
.hero-text{font-size:12px;line-height:18px;margin-top:17px;max-width:290px}

.btn{display:flex;align-items:center;justify-content:center;width:127px;height:31px;color:var(--white);
  font-size:9.5px;font-weight:800;text-decoration:none;letter-spacing:.2px;
  background:linear-gradient(90deg,var(--blue) 0%,var(--blue-bright) 100%);
  clip-path:polygon(14% 0,100% 0,86% 100%,0 100%);border-radius:4px}
.hero .btn{position:absolute;left:567px;top:270px}

.welcome{left:125px;top:608px;width:440px}
.welcome-kicker{font-size:11.5px;color:#444}
.welcome-name{font-family:'Playfair Display',serif;font-weight:700;font-size:33px;color:var(--ink);line-height:36px;margin-top:1px}
.welcome-sub{font-size:22.5px;color:var(--ink);letter-spacing:.4px;line-height:26px}
.welcome-body{margin-top:23px}
.welcome-body p{font-size:11.3px;line-height:16px;color:var(--ink);margin-bottom:9.5px}
.welcome .btn{margin-top:18px}

.name-band{left:586px;top:580px;width:58px;height:374px;background:var(--blue);display:flex;align-items:center;justify-content:center}
.name-band span{transform:rotate(-90deg);white-space:nowrap;font-family:'Playfair Display',serif;font-size:33px;
  color:transparent;-webkit-text-stroke:1px #e6f3fb;letter-spacing:.5px}
.portrait{left:644px;top:580px;width:382px;height:425px;
  background:linear-gradient(180deg,#e3ddd6 0%,#e0d7cf 55%,#e2647f 80%,#e25a7c 100%)}

.footer{left:0;top:1154px;width:1151px;height:46px;background:var(--navy);display:flex;align-items:center;justify-content:center;
  font-size:9.5px;color:#8aa3b8}
.footer b{font-weight:400;color:var(--white)}
</style>
</head>
<body>
<div class="abs gerbera-left" role="img" aria-label="Pink gerbera flower and loose petals"></div>
<div class="abs petals-top" role="img" aria-label="Scattered pink petals"></div>
<div class="abs petals-low" role="img" aria-label="Scattered pink petals"></div>
<div class="abs gerbera-right" role="img" aria-label="Red-pink gerbera flower"></div>

<div class="abs contact contact-phone">
  <span class="icon"><svg width="12" height="12" viewBox="0 0 24 24"><path fill="#fff" d="M6.6 10.8a15 15 0 0 0 6.6 6.6l2.2-2.2c.3-.3.7-.4 1-.2 1.1.4 2.3.6 3.6.6.6 0 1 .4 1 1V20c0 .6-.4 1-1 1A17 17 0 0 1 3 4c0-.6.4-1 1-1h3.5c.6 0 1 .4 1 1 0 1.3.2 2.5.6 3.6.1.3 0 .7-.2 1z"/></svg></span>
  <div><small>Call Rosalind:</small><strong>07700 900412</strong></div>
</div>

<div class="abs brand">
  <div class="brand-name">Rosalind Faber</div>
  <div class="brand-tag">Compassionate Psychotherapy</div>
</div>

<div class="abs contact contact-email">
  <span class="icon"><svg width="13" height="10" viewBox="0 0 26 20"><rect x="1" y="1" width="24" height="18" fill="none" stroke="#fff" stroke-width="2"/><path d="M1 1l12 10L25 1" fill="none" stroke="#fff" stroke-width="2"/></svg></span>
  <div><small>Emial:</small><strong>rf@rosalindfaber.co.uk</strong></div>
</div>

<nav class="abs nav">
  <a class="current" href="#">HOME</a>
  <a href="#">ABOUT ME</a>
  <a href="#">THERAPY</a>
  <a href="#">COMMON QUESTIONS</a>
  <a href="#">BLOG</a>
  <a href="#">CONTACT ME</a>
</nav>

<section class="abs hero">
  <div class="abs hero-art" role="img" aria-label="Trees shaped like heads on a hillside, half under calm sea water"></div>
  <div class="abs hero-copy">
    <div class="hero-kicker">I am Passionate</div>
    <h1 class="hero-title">About Improving Mental Health</h1>
    <p class="hero-text">I have over 10 years’ experience of dealing with addictions.</p>
  </div>
  <a class="btn" href="#">ABOUT US</a>
</section>

<section class="abs welcome">
  <div class="welcome-kicker">Welcome To</div>
  <h2 class="welcome-name">Rosalind Faber</h2>
  <div class="welcome-sub">Compassionate Psychotherapy</div>
  <div class="welcome-body">
    <p>Taking the first steps towards engaging in therapy can be a very personal journey.</p>
    <p>Whilst, it can be challenging, I will ensure to make this journey as safe and as comfortable for you as possible.</p>
    <p>Psychotherapy can help you see your current situation in new light, depth and clarity. It can change old and unhelpful perspectives and feelings about yourself and your life, and ultimately help you make positive changes. It might be the most important journey you’ll ever make.</p>
    <p>I provide a and non-judgmental space where any issues can be explored in complete confidentiality.</p>
    <p>My practice is based in Ashcombe, where the room is homely, comfortable and welcoming. I believe a good environment contributes to great therapy. Alternately, I am also available to provide therapy online, if this environment is more accommodating for my clients.</p>
    <p>I am passionate about improving mental health and committed to offering therapy to all individuals regardless of their age, race, culture, disability, sexual orientation, or socio-economic background.</p>
  </div>
  <a class="btn" href="#">READ MORE</a>
</section>

<div class="abs name-band"><span>ROSALIND FABER</span></div>
<div class="abs portrait" role="img" aria-label="Portrait photograph of the therapist in a pink top"></div>

<footer class="abs footer">Copyright © 2021&nbsp;<b>RosalindFaber</b>. All Rights Reserved.</footer>
</body>
</html>
```